Mobile Home Page Design for “Zarvo for Plumbers” – in Figma

PipeDashly: Fast, Reliable Emergency Plumbing at Your Fingertips

PipeDashly is a streamlined platform connecting homeowners with trusted, local plumbers for urgent repairs—whether it’s a burst pipe, leak, or blocked toilet. Designed for speed and peace of mind, our homepage will be clean, modern, and mobile-optimized to guide users from problem to solution in minutes.

Our primary users are homeowners in stressful situations who care most about price transparency and how fast help can arrive. Bookings are made exclusively online, so the user experience must instill confidence and eliminate hesitation.

The call-to-action should be immediate and persuasive—"See Prices & Book" will be prominently featured as the main CTA. Additional trust-builders could include:

A simple 3-step booking illustration (Tell us what’s wrong → See prices → Get a plumber)
Customer reviews or “Trusted by 10,000+ homeowners” badges

Display real-time availability ("Next plumber available in 40 minutes")
Price estimates upfront—with clear service types

Target Market(s)

Home Owners: 35-65 Years old.

Industry/Entity Type

Home Services.

Number of Pages Required

1 page

Font styles to use
Sans Serif

Colors
0054AA
0677BA
7BADD7
CADEEF
E8F1F8
FFF300
FFF600
FEFA6F
FFFEC7
FFFEE8

Requirements
Nice to have
• Map showing that plumbers are nearby. Trustworthy look and feel. Blue/Red or Blue/Yellow.

```html
<!DOCTYPE html>
<html lang="en">
<head>
<meta charset="utf-8">
<title>PipeDashly – Book a plumber near you</title>
<link rel="stylesheet" href="https://fonts.googleapis.com/css2?family=Figtree:wght@400;500;600;700;800&display=swap">
<style>
  :root {
    --backdrop: #eef0f3;
    --hero-blue: #2a22d6;
    --hero-deep: #1d18b8;
    --band-blue: #1f5ae6;
    --cta-red: #ff1b2d;
    --white: #ffffff;
    --ink: #24242e;
    --muted: #6b6b78;
    --rule: #e6e6ee;
  }
  * { box-sizing: border-box; margin: 0; padding: 0; }
  html, body { width: 900px; height: 1200px; overflow: hidden; }
  body {
    background: var(--backdrop);
    font-family: "Figtree", sans-serif;
    display: flex;
    justify-content: center;
  }
  .page {
    position: relative;
    width: 590px;
    height: 1200px;
    overflow: hidden;
    background: var(--white);
  }
  .hero {
    position: relative;
    height: 806px;
    background: var(--hero-blue);
    overflow: hidden;
  }
  .hero-photo {
    position: absolute;
    inset: 0;
    background:
      radial-gradient(ellipse 55% 45% at 78% 30%, rgba(120,110,255,0.55), transparent 70%),
      radial-gradient(ellipse 40% 60% at 25% 45%, rgba(90,80,240,0.45), transparent 70%),
      linear-gradient(180deg, var(--hero-blue) 0%, #3028e0 50%, var(--hero-deep) 100%);
  }
  .site-header {
    position: absolute;
    top: 40px; left: 46px; right: 40px;
    display: flex;
    justify-content: space-between;
    align-items: center;
  }
  .brand {
    color: var(--white);
    font-weight: 800;
    font-size: 32px;
    letter-spacing: -0.5px;
  }
  .menu-toggle { width: 46px; height: 24px; }
  .availability-pill {
    position: absolute;
    top: 410px; left: 26px;
    display: flex; align-items: center; gap: 14px;
    height: 64px;
    padding: 0 28px 0 20px;
    border: 1.5px solid rgba(255,255,255,0.7);
    border-radius: 32px;
    color: var(--white);
    font-size: 19px;
    font-weight: 600;
  }
  .availability-pill svg { width: 28px; height: 28px; }
  .headline {
    position: absolute;
    top: 490px; left: 24px; right: 24px;
    color: var(--white);
    font-size: 52px;
    font-weight: 700;
    line-height: 1.3;
    letter-spacing: -0.5px;
  }
  .headline svg { width: 26px; height: 38px; vertical-align: -4px; }
  .book-button {
    position: absolute;
    top: 666px; left: 20px; right: 20px;
    height: 88px;
    background: var(--cta-red);
    border-radius: 6px;
    color: var(--white);
    font-size: 24px;
    font-weight: 600;
    display: flex; align-items: center; justify-content: center; gap: 18px;
  }
  .book-button svg { width: 26px; height: 22px; }
  .trust-band {
    height: 130px;
    background: var(--band-blue);
    display: flex; align-items: center;
    padding: 0 30px 0 26px;
    color: var(--white);
  }
  .trust-band .tick { width: 24px; height: 20px; margin-right: 28px; flex: none; }
  .trust-copy { font-size: 19px; font-weight: 600; line-height: 1.45; flex: 1; }
  .rating { text-align: center; }
  .rating-score { font-size: 50px; font-weight: 700; line-height: 1; }
  .rating-stars { display: flex; gap: 4px; margin-top: 8px; }
  .rating-stars svg { width: 13px; height: 13px; }
  .qualities { padding: 40px 0 0; }
  .qualities-label {
    padding-left: 30px;
    font-size: 14px;
    letter-spacing: 0.4px;
    color: var(--muted);
    text-transform: uppercase;
  }
  .quality-row {
    margin-top: 38px;
    border-top: 1px solid var(--rule);
    height: 112px;
    display: flex; align-items: center;
    padding-left: 40px;
  }
  .quality-row .icon { width: 44px; height: 44px; flex: none; }
  .quality-text { margin-left: 175px; }
  .quality-title { font-size: 28px; font-weight: 500; color: var(--ink); }
  .quality-sub { font-size: 16px; color: var(--muted); margin-top: 2px; }
  .quality-row + .quality-row { margin-top: 0; }
</style>
</head>
<body>
  <main class="page">
    <section class="hero">
      <div class="hero-photo" role="img" aria-label="Photo of a plumber working on pipes, tinted blue"></div>

      <header class="site-header">
        <span class="brand">PipeDashly</span>
        <svg class="menu-toggle" viewBox="0 0 46 24" aria-label="Menu">
          <rect x="0" y="4" width="46" height="3" rx="1.5" fill="#fff"/>
          <rect x="0" y="17" width="46" height="3" rx="1.5" fill="#fff"/>
          <circle cx="41" cy="1.5" r="1.5" fill="#ff1b2d"/>
        </svg>
      </header>

      <div class="availability-pill">
        <svg viewBox="0 0 28 28" fill="none" stroke="#fff" stroke-width="2" stroke-linecap="round">
          <circle cx="6" cy="22" r="3"/>
          <circle cx="22" cy="6" r="3"/>
          <path d="M6 19V10a4 4 0 0 1 8 0v8a4 4 0 0 0 8 0V9"/>
        </svg>
        <span>• 12 Plumbers on-call near you</span>
      </div>

      <h1 class="headline">Book a plumber<br>near you - fast
        <svg viewBox="0 0 26 38"><path d="M16 0 2 22h10l-4 16L24 14H14z" fill="#ff1b2d"/></svg>
      </h1>

      <a class="book-button">Book Now
        <svg viewBox="0 0 26 22" fill="none" stroke="#fff" stroke-width="2.6" stroke-linecap="round" stroke-linejoin="round">
          <path d="M2 11h21M14 2l9 9-9 9"/>
        </svg>
      </a>
    </section>

    <section class="trust-band">
      <svg class="tick" viewBox="0 0 24 20" fill="none" stroke="#fff" stroke-width="2.6" stroke-linecap="round" stroke-linejoin="round">
        <path d="M3 10l6 6L21 3"/>
      </svg>
      <p class="trust-copy">Get an instant response from<br>a trusted plumber 24/7</p>
      <div class="rating">
        <div class="rating-score">4.9</div>
        <div class="rating-stars">
          <svg viewBox="0 0 10 10"><path d="M5 0l1.5 3.2 3.5.4-2.6 2.4.7 3.5L5 7.8 1.9 9.5l.7-3.5L0 3.6l3.5-.4z" fill="#fff"/></svg>
          <svg viewBox="0 0 10 10"><path d="M5 0l1.5 3.2 3.5.4-2.6 2.4.7 3.5L5 7.8 1.9 9.5l.7-3.5L0 3.6l3.5-.4z" fill="#fff"/></svg>
          <svg viewBox="0 0 10 10"><path d="M5 0l1.5 3.2 3.5.4-2.6 2.4.7 3.5L5 7.8 1.9 9.5l.7-3.5L0 3.6l3.5-.4z" fill="#fff"/></svg>
          <svg viewBox="0 0 10 10"><path d="M5 0l1.5 3.2 3.5.4-2.6 2.4.7 3.5L5 7.8 1.9 9.5l.7-3.5L0 3.6l3.5-.4z" fill="#fff"/></svg>
          <svg viewBox="0 0 10 10"><path d="M5 0l1.5 3.2 3.5.4-2.6 2.4.7 3.5L5 7.8 1.9 9.5l.7-3.5L0 3.6l3.5-.4z" fill="#fff"/></svg>
        </div>
      </div>
    </section>

    <section class="qualities">
      <p class="qualities-label">All our plumbers are</p>

      <div class="quality-row">
        <svg class="icon" viewBox="0 0 44 44" fill="none" stroke="#24242e" stroke-width="2">
          <path d="M22 3l5 4 6-1 2 6 5 4-3 6 3 6-5 4-2 6-6-1-5 4-5-4-6 1-2-6-5-4 3-6-3-6 5-4 2-6 6 1z"/>
          <text x="22" y="28" text-anchor="middle" font-family="Figtree, sans-serif" font-size="14" font-weight="700" fill="#24242e" stroke="none">5</text>
        </svg>
        <div class="quality-text">
          <div class="quality-title">Min 5 Yrs</div>
          <div class="quality-sub">in experience</div>
        </div>
      </div>

      <div class="quality-row">
        <svg class="icon" viewBox="0 0 44 44" fill="none" stroke="#24242e" stroke-width="2">
          <circle cx="22" cy="14" r="7"/>
          <path d="M8 38c2-8 8-12 14-12s12 4 14 12"/>
        </svg>
        <div class="quality-text">
          <div class="quality-title">Vetted</div>
        </div>
      </div>
    </section>
  </main>
</body>
</html>
```